Carpal Tunnel - PPC Landing Page

We need to do a SINGLE page landing page for a doctor who specializes in Carpal Tunnel syndrome - please research if you're not familiar - it's very common.

Landing page essentials:
Must have a form in upper right hand corner:
Form title: "Get a free diagnosis."
Form inputs: Name, Phone, Email, Requested Appointment time

Page is for PPC, so needs to be simple and light on content. Content has been provided and attached to this project.

No navigation, just a single page.

Industry/Entity Type

Health

Coding

Coded - Design and coding required

Number of Pages Required

1 page

Requirements
Must have
• Elegant look - Conversion optimized for form and phone
• Responsive design.
Should not have
• Old outdated images.

```html
<!DOCTYPE html>
<html lang="en">
<head>
<meta charset="utf-8">
<title>Carpal Tunnel Syndrome – Landing Page</title>
<link rel="stylesheet" href="https://fonts.googleapis.com/css2?family=Open+Sans:wght@300;400;600;700&display=swap">
<style>
:root{
  --blue:#1e88e5;
  --blue-dark:#1565c0;
  --ink:#333;
  --muted:#777;
  --panel:rgba(40,40,45,.82);
  --grey-band:#e8e8e8;
  --card-dark:#3d3d3d;
  --footer:#5a5a5a;
  --footer-bottom:#3c3c3c;
  --white:#fff;
}
*{box-sizing:border-box;margin:0;padding:0}
html,body{width:705px;height:1200px;overflow:hidden}
body{font-family:"Open Sans",Arial,sans-serif;color:var(--ink);background:var(--white);font-size:9px}
.site-header{height:70px;display:flex;align-items:center;padding-left:290px;gap:8px}
.brand-mark{width:30px;height:30px;border-radius:50%;background:var(--blue)}
.brand-name{font-size:15px;font-weight:400;line-height:16px;color:#444;letter-spacing:.5px}
.main-nav{height:20px;background:var(--blue);display:flex;align-items:center;padding:0 55px;color:var(--white);font-size:8px}
.main-nav ul{list-style:none;display:flex;gap:38px;flex:1}
.nav-tools{display:flex;gap:22px;align-items:center}
.hero{position:relative;height:285px;background:linear-gradient(110deg,#b9b6b1 0%,#d9d6d1 40%,#8f8c88 100%)}
.hero-text{position:absolute;left:55px;top:110px;color:var(--white)}
.hero-text h1{font-size:26px;font-weight:400;letter-spacing:.5px}
.hero-text p{font-size:24px;font-weight:300}
.lead-form{position:absolute;right:55px;top:12px;width:180px;height:245px;background:var(--panel);padding:14px 12px;color:var(--white)}
.lead-form h2{font-size:15px;font-weight:400;text-align:center;margin-bottom:12px}
.field{display:block;width:100%;height:18px;background:var(--white);border:0;margin-bottom:11px;font:7px "Open Sans",sans-serif;color:#999;padding:0 6px;line-height:18px}
.field-row{display:flex;gap:6px}
.field-row .field{flex:1}
.submit{display:block;width:100%;height:19px;background:var(--blue);color:var(--white);font-size:8px;text-align:center;line-height:19px;margin-top:4px}
.dots{display:flex;justify-content:center;gap:4px}
.dot{width:5px;height:5px;border-radius:50%;background:#ccc}
.dot.active{background:var(--blue)}
.hero .dots{position:absolute;bottom:8px;left:0;right:0}
.about{height:150px;padding:20px 55px 0;text-align:center}
.section-title{font-size:16px;font-weight:400;color:#444;margin-bottom:4px}
.title-rule{width:40px;height:2px;background:var(--blue);margin:0 auto 12px}
.about p{font-size:7px;line-height:11px;color:var(--muted)}
.conditions{height:400px;background:var(--grey-band);padding:22px 55px 0;text-align:center}
.conditions .section-title{margin-bottom:22px}
.grid{display:grid;grid-template-columns:repeat(3,1fr);grid-template-rows:repeat(2,135px);gap:4px}
.card{padding:16px 14px;color:var(--white);text-align:center}
.card h3{font-size:11px;font-weight:400;line-height:14px;margin-bottom:8px}
.card p{font-size:6.5px;line-height:9px;margin-bottom:8px}
.card-blue{background:var(--blue)}
.card-dark{background:var(--card-dark)}
.read-more{display:inline-block;padding:3px 12px;font-size:7px;background:var(--blue-dark);color:var(--white)}
.card-dark .read-more{background:var(--blue)}
.photo{background:linear-gradient(135deg,#d8cfc6,#f1ece6 60%,#b9aea3)}
.conditions .dots{justify-content:flex-end;margin-top:10px}
.sprains{height:150px;padding:22px 55px 0;display:flex;gap:30px}
.sprains-text{flex:1}
.sprains-text h2{font-size:15px;font-weight:400;color:#444;margin-bottom:10px}
.sprains-text p{font-size:6.5px;line-height:10px;color:var(--muted)}
.video{position:relative;width:220px;height:110px;background:linear-gradient(135deg,#4a2a2e,#8a4a48 55%,#2c1d22)}
.video-play{position:absolute;left:50%;top:50%;width:24px;height:17px;margin:-8px 0 0 -12px;background:#cc2222;border-radius:4px}
.video-play:after{content:"";position:absolute;left:9px;top:4px;border-left:7px solid var(--white);border-top:4.5px solid transparent;border-bottom:4.5px solid transparent}
.site-footer{height:80px;background:var(--footer);display:flex;align-items:center;padding:0 55px;color:#ddd;font-size:7px}
.contact{flex:1;display:flex;align-items:center;gap:8px}
.contact:nth-child(2){justify-content:center}
.contact:nth-child(3){justify-content:flex-end}
.contact svg{flex:none}
.contact strong{display:block;font-weight:600;color:var(--white)}
.footer-bottom{height:45px;background:var(--footer-bottom);display:flex;align-items:center;padding:0 55px;color:#bbb;font-size:6.5px}
.footer-bottom .legal{flex:1}
.socials{display:flex;gap:5px}
.socials span{width:9px;height:9px;background:#999}
</style>
</head>
<body>
<header class="site-header">
  <span class="brand-mark"></span>
  <span class="brand-name">Carpal Tunnel<br>Syndrome</span>
</header>
<nav class="main-nav">
  <ul><li>Home</li><li>About</li><li>Special treatments</li><li>Services</li><li>Blog</li><li>Contact us</li></ul>
  <div class="nav-tools"><span>Register</span><span>Search</span></div>
</nav>

<section class="hero">
  <div role="img" aria-label="Doctor examining a patient's wrist" style="position:absolute;inset:0"></div>
  <div class="hero-text">
    <h1>CARPAL TUNNEL SYNDROME</h1>
    <p>one of the most commonly</p>
  </div>
  <form class="lead-form">
    <h2>Get a free diagnosis</h2>
    <span class="field">Enter Name</span>
    <span class="field">Enter Phone</span>
    <span class="field">Enter Email</span>
    <div class="field-row"><span class="field">Date</span><span class="field">Time</span></div>
    <span class="submit">Submit</span>
  </form>
  <div class="dots"><span class="dot active"></span><span class="dot"></span><span class="dot"></span></div>
</section>

<section class="about">
  <h2 class="section-title">What is Carpal Tunnel Syndrome</h2>
  <div class="title-rule"></div>
  <p>Carpal tunnel syndrome is one of the most common conditions treated in hand surgery. It develops when the median nerve is squeezed as it passes through the wrist, causing numbness, tingling and weakness in the thumb, index and middle fingers. Symptoms often begin at night and, left untreated, can lead to lasting loss of grip strength and fine motor control.</p>
</section>

<section class="conditions">
  <h2 class="section-title">Other conditions treated by Dr. Holt:</h2>
  <div class="grid">
    <article class="card card-blue">
      <h3>Cubital Tunnel Syndrome<br>(Cell Phone Elbow)</h3>
      <p>Similar to carpal tunnel syndrome, cubital tunnel syndrome is a condition brought on by increased pressure on the ulnar nerve.</p>
      <span class="read-more">Read more</span>
    </article>
    <div class="photo" role="img" aria-label="Hands holding a patient's wrist"></div>
    <article class="card card-blue">
      <h3>DeQuervains<br>Tenosynovitis</h3>
      <p>Also known as first dorsal compartment tendonitis, this is one of the most common hand problems seen by our team.</p>
      <span class="read-more">Read more</span>
    </article>
    <div class="photo" role="img" aria-label="Therapist treating a patient's hand"></div>
    <article class="card card-dark">
      <h3>Dupuytren's<br>Disease</h3>
      <p>Dupuytren's disease is caused by an abnormal thickening in the palm and fingers. The cords slowly pull the fingers inward.</p>
      <span class="read-more">Read more</span>
    </article>
    <div class="photo" role="img" aria-label="Close-up of a hand exam"></div>
  </div>
  <div class="dots"><span class="dot active"></span><span class="dot"></span></div>
</section>

<section class="sprains">
  <div class="sprains-text">
    <h2>Hand Sprains</h2>
    <p>Do you have pain and swelling in your wrist after a fall or twist? A sprain stretches or tears the ligaments that hold the joint together. Even a mild sprain can limit movement for weeks, so an early exam helps rule out fractures and speeds recovery. Our clinic offers same-week appointments.</p>
  </div>
  <div class="video" role="img" aria-label="Video about hand anatomy">
    <span class="video-play"></span>
  </div>
</section>

<footer>
  <div class="site-footer">
    <div class="contact">
      <svg width="16" height="20" viewBox="0 0 16 20"><path d="M8 0a7 7 0 0 0-7 7c0 5 7 13 7 13s7-8 7-13a7 7 0 0 0-7-7z" fill="#ddd"/><circle cx="8" cy="7" r="2.5" fill="#5a5a5a"/></svg>
      <div><strong>Address</strong>145 Elm Row, Fairview 10482</div>
    </div>
    <div class="contact">
      <svg width="16" height="16" viewBox="0 0 16 16"><path d="M3 1l3 3-2 2c1 2 3 4 5 5l2-2 3 3-2 3C6 14 2 10 1 3z" fill="#ddd"/></svg>
      <div><strong>Phone number</strong>+1 555 014 2286</div>
    </div>
    <div class="contact">
      <svg width="18" height="13" viewBox="0 0 18 13"><rect x="0.5" y="0.5" width="17" height="12" fill="none" stroke="#ddd"/><path d="M1 1l8 6 8-6" fill="none" stroke="#ddd"/></svg>
      <div><strong>Email</strong>info@wristclinic.example</div>
    </div>
  </div>
  <div class="footer-bottom">
    <span class="legal">© 2024 Copyright. Privacy Policy · Terms of Use</span>
    <div class="socials"><span></span><span></span><span></span><span></span></div>
  </div>
</footer>
</body>
</html>
```